Data Management as a Service Powerpoint Design

We need the attached PowerPoint presentation redesigning including all graphics, icons, images, and graphs. The messaging in the content should remain however artistic flair can be used to change any diagram/icon/graph layout.
For preferred colour scheme and brand continuity our website is: tavexo.com, however we are open to new colours/scheme.
The only stipulation is that the hexagon layout on the DMaaS product slide (slide 4) must remain. All other icons must be changed. We would also like this to be editable, and not full-slide static images pasted from another graphics suite.

```html
<!DOCTYPE html>
<html lang="en">
<head>
<meta charset="utf-8">
<title>TAVEXO – Data Management as a Service deck</title>
<link rel="stylesheet" href="https://fonts.googleapis.com/css2?family=Lexend:wght@300;400;500;600&display=swap">
<style>
:root{
  --navy:#1c2b45;
  --navy-deep:#16233a;
  --teal:#2a9fae;
  --teal-soft:#6fc2cb;
  --pink:#d63a7e;
  --orange:#ef8a4a;
  --green:#4d9a2c;
  --ink:#333a45;
  --grey:#8a8f98;
  --light:#e9ebef;
  --paper:#ffffff;
}
*{margin:0;padding:0;box-sizing:border-box}
html,body{width:778px;height:1200px;overflow:hidden;background:var(--paper)}
body{position:relative;font-family:"Lexend",sans-serif;color:var(--ink)}
.slide{position:absolute;width:303px;height:171px;background:var(--paper);box-shadow:0 1px 4px rgba(0,0,0,.28)}
.col-l{left:53px}.col-r{left:413px}
.row1{top:80px}.row2{top:294px}.row3{top:508px}.row4{top:722px}.row5{top:936px}
.slide svg{display:block;width:303px;height:171px}
svg text{font-family:"Lexend",sans-serif}
.brand{font-weight:600;font-size:11px;letter-spacing:2px;fill:var(--navy)}
.foot{font-size:7px;fill:var(--grey)}
.lbl{font-size:10.5px;text-anchor:middle}
.defs{position:absolute;width:0;height:0}
</style>
</head>
<body>

<svg class="defs" aria-hidden="true">
  <defs>
    <polygon id="hex" points="-50,0 -25,-43.3 25,-43.3 50,0 25,43.3 -25,43.3"/>
    <linearGradient id="g-navy" x1="0" y1="0" x2="1" y2="1"><stop offset="0" stop-color="#1a2e4a"/><stop offset="1" stop-color="#12203a"/></linearGradient>
    <linearGradient id="g-navyteal" x1="0" y1="0" x2="1" y2="0"><stop offset="0" stop-color="#173550"/><stop offset="1" stop-color="#1e7f86"/></linearGradient>
    <linearGradient id="g-grey" x1="0" y1="0" x2="1" y2="1"><stop offset="0" stop-color="#f2f3f5"/><stop offset="1" stop-color="#cfd3d9"/></linearGradient>
    <linearGradient id="g-wave-pink" x1="0" y1="0" x2="1" y2="1"><stop offset="0" stop-color="#fff" stop-opacity="0"/><stop offset=".5" stop-color="#f6c9d9"/><stop offset="1" stop-color="#fbe5ec"/></linearGradient>
    <linearGradient id="g-wave-teal" x1="0" y1="0" x2="1" y2="1"><stop offset="0" stop-color="#fff" stop-opacity="0"/><stop offset=".5" stop-color="#cfe7ea"/><stop offset="1" stop-color="#f3d6e1"/></linearGradient>
    <linearGradient id="g-wave-orange" x1="0" y1="0" x2="1" y2="1"><stop offset="0" stop-color="#fff" stop-opacity="0"/><stop offset=".6" stop-color="#f8d2b7"/><stop offset="1" stop-color="#fbe6d7"/></linearGradient>
    <linearGradient id="g-photo-warm" x1="0" y1="0" x2="1" y2="1"><stop offset="0" stop-color="#d9d6d3"/><stop offset="1" stop-color="#8a8f98"/></linearGradient>

    <symbol id="i-person" viewBox="-12 -12 24 24" overflow="visible">
      <circle r="11" fill="none" stroke="currentColor" stroke-width="1.6"/>
      <circle cy="-3" r="3.6" fill="currentColor"/>
      <path d="M-6.5 7 Q0 -1 6.5 7Z" fill="currentColor"/>
    </symbol>
    <symbol id="i-db" viewBox="-14 -16 28 32" overflow="visible">
      <g fill="currentColor"><ellipse cy="-11" rx="12" ry="4"/><path d="M-12 -8 v6 a12 4 0 0 0 24 0 v-6 a12 4 0 0 1 -24 0Z"/><path d="M-12 1 v6 a12 4 0 0 0 24 0 v-6 a12 4 0 0 1 -24 0Z"/><path d="M-12 10 v2 a12 4 0 0 0 24 0 v-2 a12 4 0 0 1 -24 0Z"/></g>
    </symbol>
    <symbol id="i-env" viewBox="-18 -12 36 24" overflow="visible">
      <rect x="-17" y="-11" width="34" height="22" fill="none" stroke="currentColor" stroke-width="2"/>
      <polyline points="-17,-11 0,3 17,-11" fill="none" stroke="currentColor" stroke-width="2"/>
      <line x1="-17" y1="11" x2="-4" y2="0" stroke="currentColor" stroke-width="2"/><line x1="17" y1="11" x2="4" y2="0" stroke="currentColor" stroke-width="2"/>
    </symbol>
    <symbol id="i-grid" viewBox="-18 -16 36 32" overflow="visible">
      <g fill="none" stroke="currentColor" stroke-width="2">
        <rect x="-15" y="-15" width="24" height="24"/><line x1="-7" y1="-15" x2="-7" y2="9"/><line x1="1" y1="-15" x2="1" y2="9"/><line x1="-15" y1="-7" x2="9" y2="-7"/><line x1="-15" y1="1" x2="9" y2="1"/>
        <rect x="11" y="-2" width="6" height="6"/><rect x="-19" y="9" width="6" height="6"/>
      </g>
    </symbol>
    <symbol id="i-mag" viewBox="-14 -14 28 28" overflow="visible">
      <circle cx="-2" cy="-2" r="9" fill="none" stroke="currentColor" stroke-width="2.2"/>
      <line x1="5" y1="5" x2="12" y2="12" stroke="currentColor" stroke-width="3"/>
      <polyline points="-8,-2 -5,-2 -3,-6 -1,2 1,-2 4,-2" fill="none" stroke="currentColor" stroke-width="1.5"/>
    </symbol>
    <symbol id="i-id" viewBox="-18 -12 36 24" overflow="visible">
      <rect x="-17" y="-11" width="34" height="22" rx="2" fill="currentColor"/>
      <circle cx="-8" cy="-3" r="3.5" fill="#fff"/><path d="M-14 7 Q-8 -1 -2 7Z" fill="#fff"/>
      <g stroke="#fff" stroke-width="2"><line x1="2" y1="-5" x2="13" y2="-5"/><line x1="2" y1="0" x2="13" y2="0"/><line x1="2" y1="5" x2="13" y2="5"/></g>
    </symbol>
    <symbol id="i-cloud" viewBox="-24 -14 48 28" overflow="visible">
      <path d="M-18 12 a8 8 0 0 1 0-16 a11 11 0 0 1 20-6 a9 9 0 0 1 14 6 a8 8 0 0 1 2 16Z" fill="currentColor"/>
    </symbol>
    <symbol id="i-conv" viewBox="-18 -16 36 32" overflow="visible">
      <g fill="none" stroke="currentColor" stroke-width="2"><rect x="-17" y="-15" width="14" height="30"/><rect x="3" y="-15" width="14" height="30"/>
      <polyline points="-10,0 10,0"/><polyline points="5,-5 10,0 5,5"/></g>
    </symbol>
    <symbol id="i-flow" viewBox="-16 -16 32 32" overflow="visible">
      <g fill="none" stroke="currentColor" stroke-width="1.8"><path d="M-14 -6 h12 v-6 l12 12 -12 12 v-6 h-12Z"/></g>
    </symbol>
    <symbol id="i-gear" viewBox="-14 -14 28 28" overflow="visible">
      <g fill="none" stroke="currentColor" stroke-width="2"><circle r="7"/><circle r="2.5"/>
      <path d="M0 -12 v4 M0 8 v4 M-12 0 h4 M8 0 h4 M-8.5 -8.5 l3 3 M5.5 5.5 l3 3 M8.5 -8.5 l-3 3 M-5.5 5.5 l-3 3"/></g>
    </symbol>
    <symbol id="i-laptop" viewBox="-26 -18 52 36" overflow="visible">
      <rect x="-19" y="-16" width="38" height="26" fill="none" stroke="currentColor" stroke-width="2.5"/>
      <polyline points="-12,4 -5,-4 1,0 9,-9" fill="none" stroke="var(--pink)" stroke-width="2"/>
      <rect x="-25" y="12" width="50" height="3" fill="currentColor"/>
    </symbol>
  </defs>
</svg>

<!-- Slide 1: cover -->
<section class="slide col-l row1" aria-label="Cover slide">
<svg viewBox="0 0 606 342">
  <rect width="606" height="342" fill="#fff"/>
  <g role="img" aria-label="Abstract dark hexagon network imagery">
    <polygon points="228,0 525,0 458,150 296,150" fill="url(#g-navy)"/>
    <polygon points="296,172 458,172 530,342 228,342" fill="url(#g-navy)"/>
    <polygon points="472,162 545,22 606,22 606,302 545,302" fill="url(#g-navyteal)"/>
  </g>
  <text x="40" y="102" font-size="31" font-weight="600" fill="var(--navy)" letter-spacing="3">TAVEXO</text>
  <g font-size="29" fill="var(--ink)">
    <text x="40" y="140">Data</text><text x="40" y="173">Management</text><text x="40" y="206">as a Service</text>
  </g>
  <g font-size="12.5" fill="var(--ink)">
    <text x="40" y="231">Delivering enterprise class data</text><text x="40" y="244">and application management</text><text x="40" y="257">solutions as a service</text>
  </g>
</svg>
</section>

<!-- Slide 2: application -->
<section class="slide col-r row1" aria-label="DMaaS Application">
<svg viewBox="0 0 606 342">
  <rect width="606" height="342" fill="#fff"/>
  <g role="img" aria-label="Stack of light grey hexagon photos of security padlocks">
    <polygon points="0,0 120,0 92,58 0,58" fill="url(#g-grey)"/>
    <polygon points="0,66 60,66 92,120 60,175 0,175" fill="#d8dbe0"/>
    <polygon points="35,120 118,120 132,170 100,228 35,228" fill="#bfc4cb"/>
    <polygon points="0,236 60,236 92,290 60,342 0,342" fill="url(#g-grey)"/>
  </g>
  <text class="brand" x="512" y="40">TAVEXO</text>
  <text x="236" y="78" font-size="21" fill="var(--ink)">DMaaS Application</text>
  <circle cx="475" cy="70" r="9" fill="none" stroke="#5a6fd6" stroke-width="1.6"/>
  <g stroke="var(--navy)" stroke-width="9" fill="#f4f5f7">
    <use href="#hex" transform="translate(210,170) scale(1.1)"/>
    <use href="#hex" transform="translate(357,170) scale(1.1)"/>
    <use href="#hex" transform="translate(503,170) scale(1.1)"/>
  </g>
  <use href="#i-gear" x="180" y="140" width="40" height="40" color="var(--navy)"/>
  <use href="#i-gear" x="208" y="158" width="26" height="26" color="var(--navy)"/>
  <circle cx="357" cy="168" r="18" fill="none" stroke="var(--pink)" stroke-width="2.5"/>
  <path d="M357 152 v32 M345 160 h24 M345 176 h24" stroke="var(--pink)" stroke-width="1.8"/>
  <use href="#i-person" x="483" y="148" width="40" height="40" color="var(--navy)"/>
  <g class="lbl" font-size="12" fill="var(--ink)">
    <text x="210" y="248">Automation</text><text x="357" y="248">AI</text><text x="503" y="248">Service</text>
  </g>
  <text class="foot" x="95" y="330">© 2023 TAVEXO. Public Security Policy | Privacy Policy</text>
  <text class="foot" x="565" y="330" text-anchor="end">www.tavexo.com | 3</text>
</svg>
</section>

<!-- Slide 3: DMaaS hexagon -->
<section class="slide col-l row2" aria-label="DMaaS overview">
<svg viewBox="0 0 606 342">
  <rect width="606" height="342" fill="#fff"/>
  <text class="brand" x="512" y="40">TAVEXO</text>
  <g stroke="var(--navy)" stroke-width="7" fill="url(#g-grey)">
    <use href="#hex" transform="translate(164,80) scale(.9)"/>
    <use href="#hex" transform="translate(89,126) scale(.9)"/>
    <use href="#hex" transform="translate(238,126) scale(.9)"/>
    <use href="#hex" transform="translate(164,170) scale(.9)"/>
    <use href="#hex" transform="translate(89,215) scale(.9)"/>
    <use href="#hex" transform="translate(238,215) scale(.9)"/>
    <use href="#hex" transform="translate(164,260) scale(.9)"/>
  </g>
  <g class="lbl" fill="var(--ink)">
    <text x="164" y="84">EDRMS</text>
    <text x="89" y="124">Data</text><text x="89" y="136">Mapping</text>
    <text x="238" y="129" font-size="8.5">Assessment</text>
    <text x="164" y="174">DMaaS</text>
    <text x="89" y="219">Lifecycle</text>
    <text x="238" y="218" font-size="8.5">Classification</text>
    <text x="164" y="264">Privacy</text>
  </g>
  <text x="364" y="108" font-size="27" fill="var(--ink)">DMaaS</text>
  <text x="364" y="133" font-size="16.5" fill="var(--teal)">Data Management</text>
  <text x="364" y="154" font-size="16.5" fill="var(--teal)">as a Service</text>
  <g font-size="8.3" fill="var(--ink)">
    <text x="364" y="187"><tspan font-weight="600">Lorem Ipsum</tspan> is simply dummy text of</text>
    <text x="364" y="197">the printing and typesetting industry.</text>
    <text x="364" y="207">Lorem Ipsum has been the industry's</text>
    <text x="364" y="217">standard dummy text ever since the</text>
    <text x="364" y="227">1500s, when an unknown printer took a</text>
    <text x="364" y="237">galley of type and scrambled it to make</text>
    <text x="364" y="247">a type specimen book. It has survived</text>
    <text x="364" y="257">not only five centuries, but also the leap</text>
    <text x="364" y="267">into electronic typesetting,</text>
  </g>
  <text class="foot" x="93" y="330">© 2023 TAVEXO. Public Security Policy | Privacy Policy</text>
  <text class="foot" x="560" y="330" text-anchor="end">www.tavexo.com | 4</text>
</svg>
</section>

<!-- Slide 4: architecture -->
<section class="slide col-r row2" aria-label="Deployment architecture">
<svg viewBox="0 0 606 342">
  <rect width="606" height="342" fill="#fff"/>
  <path d="M0 342 C120 250 300 250 606 180 V342Z" fill="url(#g-wave-orange)" role="img" aria-label="Soft dotted wave background"/>
  <text class="brand" x="512" y="40">TAVEXO</text>
  <g role="img" aria-label="Cloud server photo in teal hexagon">
    <use href="#hex" transform="translate(135,90) scale(1.25)" fill="#4aa5ae"/>
  </g>
  <use href="#i-cloud" x="108" y="50" width="56" height="32" color="#fff"/>
  <use href="#i-db" x="95" y="90" width="26" height="30" color="#fff"/>
  <g role="img" aria-label="Office photo in pink hexagon">
    <use href="#hex" transform="translate(215,205) scale(1.7)" fill="#d8609a"/>
  </g>
  <use href="#i-db" x="100" y="185" width="30" height="34" color="#fff"/>
  <use href="#i-flow" x="150" y="195" width="34" height="34" color="#fff"/>
  <g role="img" aria-label="Orange hexagon with console imagery">
    <use href="#hex" transform="translate(470,170) scale(2)" fill="#e7884c"/>
  </g>
  <text x="195" y="50" font-size="10.5" letter-spacing="1.5" fill="var(--teal)">Customer's</text>
  <text x="195" y="62" font-size="10.5" letter-spacing="1.5" fill="var(--teal)">Public Cloud</text>
  <text x="35" y="168" font-size="10.5" letter-spacing="1.5" fill="var(--pink)">Customer's</text>
  <text x="35" y="180" font-size="10.5" letter-spacing="1.5" fill="var(--pink)">Premise</text>
  <line x1="190" y1="82" x2="350" y2="155" stroke="var(--teal)" stroke-width="1.6"/>
  <polygon points="352,156 342,156 346,148" fill="var(--teal)"/>
  <line x1="290" y1="205" x2="350" y2="162" stroke="var(--pink)" stroke-width="1.6"/>
  <text x="270" y="105" font-size="7" fill="var(--teal)" transform="rotate(25 270 105)">Metadata Reporting</text>
  <text x="295" y="188" font-size="7" fill="var(--pink)" transform="rotate(-38 295 188)">Metadata Reporting</text>
  <g fill="#fff" font-size="8.5">
    <text x="385" y="130" font-weight="600" letter-spacing="1">TAVEXO</text>
    <text x="388" y="172" font-size="9">Indexing and</text><text x="395" y="183" font-size="9">AI engine</text>
    <text x="465" y="118">Administration</text><text x="478" y="129">Console</text>
    <text x="390" y="155" font-size="9">◈ ◈</text>
    <text x="200" y="180">VM /</text><text x="195" y="191">Physical</text><text x="195" y="202">Appliance</text>
    <text x="200" y="240" font-size="7">• Read</text><text x="205" y="249" font-size="7">source</text><text x="205" y="258" font-size="7">data</text>
    <text x="200" y="267" font-size="7">• Tunnel</text><text x="205" y="276" font-size="7">Encryption</text>
  </g>
  <rect x="196" y="210" width="32" height="10" fill="#fff"/>
  <g fill="#fff">
    <circle cx="490" cy="90" r="7"/><rect x="505" y="85" width="14" height="12"/>
    <circle cx="485" cy="212" r="9"/><rect x="512" y="195" width="26" height="16" rx="2"/>
    <circle cx="545" cy="204" r="9"/><rect x="470" y="228" width="26" height="14"/>
    <rect x="500" y="226" width="22" height="14"/><rect x="528" y="226" width="22" height="16"/>
  </g>
  <text class="foot" x="95" y="330">© 2023 TAVEXO. Public Security Policy | Privacy Policy</text>
</svg>
</section>

<!-- Slide 5: lifecycle -->
<section class="slide col-l row3" aria-label="Lifecycle">
<svg viewBox="0 0 606 342">
  <rect width="606" height="342" fill="#fff"/>
  <path d="M0 342 C80 150 300 300 606 200 V342Z" fill="url(#g-wave-pink)" role="img" aria-label="Soft dotted wave background"/>
  <text class="brand" x="512" y="40">TAVEXO</text>
  <g role="img" aria-label="Light grey hexagon photo"><use href="#hex" transform="translate(105,80) scale(1.2)" fill="url(#g-grey)" stroke="#fff" stroke-width="3"/></g>
  <text x="105" y="86" class="lbl" font-size="17" fill="var(--teal)">Lifecycle</text>
  <text x="65" y="178" class="lbl" fill="var(--teal)" font-size="9.5">Unstructured</text>
  <text x="65" y="190" class="lbl" fill="var(--teal)" font-size="9.5">Data Siloes</text>
  <use href="#i-db" x="132" y="140" width="30" height="34" color="var(--teal)"/>
  <use href="#i-cloud" x="180" y="142" width="64" height="38" color="var(--teal)"/>
  <use href="#i-db" x="160" y="185" width="30" height="34" color="#23545b"/>
  <use href="#i-cloud" x="80" y="198" width="64" height="38" color="var(--teal-soft)"/>
  <use href="#i-db" x="205" y="225" width="30" height="34" color="var(--teal)"/>
  <use href="#i-db" x="143" y="245" width="30" height="34" color="#23545b"/>
  <path d="M255 136 h10 v150 h-10 M265 211 h10" fill="none" stroke="var(--teal)" stroke-width="1.5"/>
  <use href="#i-laptop" x="290" y="183" width="60" height="42" color="var(--teal)"/>
  <line x1="355" y1="211" x2="385" y2="211" stroke="var(--teal)" stroke-width="1.5"/>
  <use href="#i-flow" x="400" y="193" width="34" height="34" color="var(--orange)"/>
  <line x1="445" y1="211" x2="495" y2="211" stroke="var(--teal)" stroke-width="1.5"/>
  <use href="#i-db" x="505" y="185" width="44" height="46" color="var(--teal)"/>
  <g class="lbl" fill="var(--teal)" font-size="9.5">
    <text x="320" y="248">ROT</text><text x="320" y="260">Analysis</text>
    <text x="418" y="248">Automated</text><text x="418" y="260">Remediation</text>
    <text x="525" y="248">Streamlined,</text><text x="525" y="260">Controlled</text><text x="525" y="272">Data Storage</text>
    <text x="525" y="160">Storage Vendor</text><text x="525" y="172">Agnostic</text>
  </g>
  <text class="foot" x="93" y="330">© 2023 TAVEXO. Public Security Policy | Privacy Policy</text>
</svg>
</section>

<!-- Slide 6: privacy manual -->
<section class="slide col-r row3" aria-label="Privacy manual process">
<svg viewBox="0 0 606 342">
  <rect width="606" height="342" fill="#fff"/>
  <path d="M0 342 C100 220 350 300 606 220 V342Z" fill="url(#g-wave-teal)" role="img" aria-label="Soft dotted wave background"/>
  <text class="brand" x="512" y="40">TAVEXO</text>
  <g role="img" aria-label="Hexagon photo of a person at work"><use href="#hex" transform="translate(105,80) scale(1.2)" fill="url(#g-photo-warm)" stroke="#fff" stroke-width="3" opacity=".55"/></g>
  <text x="105" y="86" class="lbl" font-size="17" fill="var(--pink)">Privacy</text>
  <g color="var(--pink)">
    <use href="#i-person" x="209" y="64" width="22" height="22"/><use href="#i-person" x="237" y="64" width="22" height="22"/><use href="#i-person" x="266" y="64" width="22" height="22"/>
    <use href="#i-mag" x="238" y="94" width="30" height="30"/>
    <use href="#i-db" x="345" y="93" width="28" height="30"/>
    <use href="#i-id" x="128" y="185" width="40" height="28"/>
    <use href="#i-conv" x="284" y="168" width="36" height="34"/>
    <use href="#i-person" x="264" y="219" width="22" height="22"/><use href="#i-person" x="291" y="219" width="22" height="22"/><use href="#i-person" x="319" y="219" width="22" height="22"/>
    <use href="#i-grid" x="398" y="166" width="40" height="36"/>
    <use href="#i-person" x="382" y="219" width="22" height="22"/><use href="#i-person" x="408" y="219" width="22" height="22"/><use href="#i-person" x="434" y="219" width="22" height="22"/>
    <use href="#i-person" x="395" y="244" width="22" height="22"/><use href="#i-person" x="421" y="244" width="22" height="22"/>
    <use href="#i-env" x="478" y="112" width="38" height="26"/>
    <use href="#i-person" x="522" y="115" width="22" height="22"/>
    <use href="#i-person" x="272" y="280" width="22" height="22"/>
  </g>
  <g stroke="var(--orange)" stroke-width="1.5" fill="none">
    <line x1="278" y1="108" x2="330" y2="108"/><line x1="352" y1="130" x2="325" y2="160"/>
    <line x1="165" y1="188" x2="215" y2="150"/><line x1="330" y1="185" x2="390" y2="185"/>
    <line x1="445" y1="182" x2="490" y2="145"/>
  </g>
  <g stroke="var(--pink)" stroke-width="1.5"><line x1="60" y1="291" x2="262" y2="291"/><line x1="390" y1="291" x2="545" y2="291"/></g>
  <circle cx="60" cy="291" r="3" fill="var(--pink)"/><circle cx="545" cy="291" r="3" fill="var(--pink)"/>
  <g class="lbl" fill="var(--pink)" font-size="9.5">
    <text x="258" y="137">E-discovery</text><text x="258" y="149">&amp; Collection</text>
    <text x="365" y="91" fill="var(--orange)">Collection Silo</text>
    <text x="148" y="231">ID check</text>
    <text x="303" y="213">Conversion</text>
    <text x="422" y="149">Manual</text><text x="422" y="161">Redaction</text>
    <text x="527" y="162">Export</text>
    <text x="340" y="289">Manual process</text><text x="340" y="301">management</text>
  </g>
  <text class="foot" x="95" y="330">© 2023 TAVEXO. Public Security Policy | Privacy Policy</text>
</svg>
</section>

<!-- Slide 7: privacy automated -->
<section class="slide col-l row4" aria-label="Privacy software automation">
<svg viewBox="0 0 606 342">
  <rect width="606" height="342" fill="#fff"/>
  <path d="M0 342 C100 220 350 300 606 220 V342Z" fill="url(#g-wave-teal)" role="img" aria-label="Soft dotted wave background"/>
  <text class="brand" x="512" y="40">TAVEXO</text>
  <g role="img" aria-label="Hexagon photo of a person at work"><use href="#hex" transform="translate(105,80) scale(1.2)" fill="url(#g-photo-warm)" stroke="#fff" stroke-width="3" opacity=".55"/></g>
  <text x="105" y="86" class="lbl" font-size="17" fill="var(--pink)">Privacy</text>
  <text x="345" y="103" class="lbl" fill="var(--pink)" font-size="10">Software Automation</text>
  <rect x="168" y="127" width="370" height="113" fill="none" stroke="var(--orange)" stroke-width="1.5" stroke-dasharray="6 4"/>
  <circle cx="352" cy="128" r="9" fill="#fff" stroke="var(--pink)" stroke-width="2"/>
  <g color="var(--pink)">
    <use href="#i-id" x="80" y="161" width="40" height="28"/>
    <use href="#i-mag" x="212" y="160" width="32" height="32"/>
    <use href="#i-grid" x="325" y="157" width="42" height="38"/>
    <use href="#i-env" x="457" y="162" width="40" height="28"/>
    <use href="#i-person" x="235" y="257" width="22" height="22"/>
  </g>
  <g stroke="var(--orange)" stroke-width="1.5"><line x1="125" y1="176" x2="200" y2="176"/><line x1="252" y1="176" x2="315" y2="176"/><line x1="378" y1="176" x2="445" y2="176"/></g>
  <g stroke="var(--pink)" stroke-width="1.5"><line x1="60" y1="268" x2="228" y2="268"/><line x1="410" y1="268" x2="538" y2="268"/></g>
  <circle cx="60" cy="268" r="3" fill="var(--pink)"/><circle cx="538" cy="268" r="3" fill="var(--pink)"/>
  <g class="lbl" fill="var(--pink)" font-size="9.5">
    <text x="100" y="207">ID check</text>
    <text x="228" y="207">E-discovery</text><text x="228" y="219">&amp; Collection</text>
    <text x="345" y="207">Redaction</text>
    <text x="477" y="207">Export</text>
    <text x="326" y="266">Self service or managed</text><text x="326" y="278">request workflow</text>
  </g>
  <text class="foot" x="93" y="330">© 2023 TAVEXO. Public Security Policy | Privacy Policy</text>
</svg>
</section>

<!-- Slide 8: automated redaction -->
<section class="slide col-r row4" aria-label="Automated redaction">
<svg viewBox="0 0 606 342">
  <rect width="606" height="342" fill="#fff"/>
  <g role="img" aria-label="Hexagon photos of people working on laptops">
    <polygon points="460,0 606,0 606,40 560,40" fill="#cfd2d6"/>
    <polygon points="462,70 520,40 580,70 580,140 520,170 462,140" fill="#9aa2ac"/>
    <polygon points="585,40 606,40 606,180 585,180" fill="#8b939c"/>
    <polygon points="462,160 520,130 560,160 560,230 520,260 462,230" fill="#b9b3ad"/>
    <polygon points="520,210 580,180 606,195 606,300 560,300" fill="#c7c3bf"/>
  </g>
  <text class="brand" x="512" y="40">TAVEXO</text>
  <g role="img" aria-label="Hexagon photo of a person at a desk"><use href="#hex" transform="translate(105,80) scale(1.2)" fill="url(#g-photo-warm)" stroke="#fff" stroke-width="3" opacity=".55"/></g>
  <text x="105" y="86" class="lbl" font-size="14" fill="var(--green)">Redaction</text>
  <rect x="273" y="38" width="186" height="264" fill="#fff" stroke="#555" stroke-width="1"/>
  <g fill="#9aa0a8">
    <rect x="400" y="62" width="48" height="2"/><rect x="412" y="70" width="36" height="2"/><rect x="420" y="78" width="28" height="2"/>
    <rect x="290" y="110" width="60" height="3"/><rect x="290" y="120" width="150" height="2"/><rect x="290" y="126" width="70" height="2"/><rect x="370" y="126" width="70" height="2"/>
    <rect x="290" y="132" width="70" height="2"/><rect x="370" y="132" width="70" height="2"/><rect x="290" y="138" width="70" height="2"/><rect x="370" y="138" width="70" height="2"/>
    <rect x="290" y="150" width="140" height="2"/><rect x="290" y="156" width="150" height="2"/>
    <rect x="290" y="185" width="40" height="2"/><rect x="290" y="193" width="150" height="2"/><rect x="290" y="199" width="150" height="2"/><rect x="290" y="205" width="120" height="2"/>
    <rect x="290" y="217" width="150" height="2"/><rect x="290" y="223" width="150" height="2"/><rect x="290" y="229" width="100" height="2"/>
    <rect x="290" y="245" width="40" height="2"/><rect x="290" y="253" width="150" height="2"/><rect x="290" y="259" width="150" height="2"/><rect x="290" y="265" width="150" height="2"/><rect x="290" y="271" width="80" height="2"/>
  </g>
  <g fill="#9bd36b">
    <rect x="425" y="86" width="23" height="3"/><rect x="290" y="124" width="22" height="4"/><rect x="300" y="136" width="26" height="4"/>
    <rect x="395" y="142" width="30" height="4"/><rect x="320" y="198" width="22" height="4"/><rect x="380" y="222" width="26" height="4"/><rect x="330" y="258" width="28" height="4"/>
  </g>
  <text x="208" y="268" class="lbl" font-size="11" font-weight="500" fill="var(--green)">Automated</text>
  <text x="211" y="282" class="lbl" font-size="11" font-weight="500" fill="var(--green)">Redaction</text>
  <text class="foot" x="95" y="330">© 2023 TAVEXO. Public Security Policy | Privacy Policy</text>
  <text class="foot" x="565" y="330" text-anchor="end">www.tavexo.com | 9</text>
</svg>
</section>

<!-- Slide 9: immutable redaction -->
<section class="slide col-l row5" aria-label="Immutable redaction">
<svg viewBox="0 0 606 342">
  <rect width="606" height="342" fill="#fff"/>
  <g role="img" aria-label="Hexagon photos of a business handshake and office">
    <polygon points="460,110 520,80 580,110 580,190 520,220 460,190" fill="#a7aeb6"/>
    <polygon points="520,200 580,170 606,185 606,300 520,300" fill="#c9b9a6"/>
    <polygon points="270,300 330,290 606,300 606,342 250,342" fill="#d5d9de"/>
    <polygon points="585,60 606,50 606,160 585,160" fill="#cfd3d8"/>
  </g>
  <text class="brand" x="512" y="40">TAVEXO</text>
  <g role="img" aria-label="Hexagon photo of a person at a desk"><use href="#hex" transform="translate(105,80) scale(1.2)" fill="url(#g-grey)" stroke="#fff" stroke-width="3"/></g>
  <text x="105" y="86" class="lbl" font-size="14" fill="#6b7079">Redaction</text>
  <rect x="273" y="38" width="186" height="264" fill="#fff" stroke="#555" stroke-width="1"/>
  <g fill="#9aa0a8">
    <rect x="400" y="62" width="48" height="2"/><rect x="412" y="70" width="36" height="2"/>
    <rect x="290" y="120" width="150" height="2"/><rect x="370" y="126" width="70" height="2"/><rect x="370" y="132" width="70" height="2"/><rect x="370" y="138" width="70" height="2"/>
    <rect x="290" y="156" width="150" height="2"/><rect x="290" y="185" width="40" height="2"/><rect x="290" y="193" width="150" height="2"/><rect x="290" y="205" width="120" height="2"/>
    <rect x="290" y="217" width="150" height="2"/><rect x="290" y="229" width="100" height="2"/><rect x="290" y="253" width="150" height="2"/><rect x="290" y="265" width="150" height="2"/>
  </g>
  <g fill="#111">
    <rect x="428" y="78" width="20" height="4"/><rect x="428" y="86" width="20" height="4"/><rect x="412" y="94" width="36" height="4"/>
    <rect x="290" y="108" width="26" height="4"/><rect x="290" y="124" width="50" height="4"/><rect x="290" y="130" width="45" height="4"/><rect x="290" y="136" width="55" height="4"/>
    <rect x="290" y="142" width="60" height="4"/><rect x="290" y="148" width="48" height="4"/>
    <rect x="320" y="198" width="22" height="4"/><rect x="290" y="210" width="30" height="4"/><rect x="380" y="222" width="26" height="4"/>
    <rect x="330" y="258" width="28" height="4"/><rect x="290" y="270" width="26" height="4"/>
  </g>
  <text x="208" y="268" class="lbl" font-size="11" font-weight="500" fill="#5d626b">Immutable</text>
  <text x="211" y="282" class="lbl" font-size="11" font-weight="500" fill="#5d626b">Redaction</text>
  <text class="foot" x="93" y="330">© 2023 TAVEXO. Public Security Policy | Privacy Policy</text>
</svg>
</section>

<!-- Slide 10: redaction workflow -->
<section class="slide col-r row5" aria-label="Redaction workflow">
<svg viewBox="0 0 606 342">
  <rect width="606" height="342" fill="#fff"/>
  <path d="M0 342 C100 220 350 300 606 220 V342Z" fill="url(#g-wave-teal)" role="img" aria-label="Soft dotted wave background"/>
  <text class="brand" x="512" y="40">TAVEXO</text>
  <g role="img" aria-label="Hexagon photo of a person at a desk"><use href="#hex" transform="translate(105,80) scale(1.2)" fill="url(#g-grey)" stroke="#fff" stroke-width="3"/></g>
  <text x="105" y="86" class="lbl" font-size="14" fill="#6b7079">Redaction</text>
  <rect x="153" y="155" width="309" height="103" fill="none" stroke="var(--pink)" stroke-width="1.5" stroke-dasharray="6 4"/>
  <line x1="410" y1="118" x2="410" y2="186" stroke="var(--pink)" stroke-width="2"/>
  <g color="var(--pink)">
    <use href="#i-person" x="399" y="84" width="22" height="22"/>
    <use href="#i-mag" x="64" y="188" width="32" height="32"/>
    <use href="#i-grid" x="390" y="186" width="40" height="36"/>
    <use href="#i-env" x="508" y="192" width="38" height="26"/>
  </g>
  <g color="var(--orange)">
    <use href="#i-flow" x="172" y="188" width="34" height="34"/>
    <use href="#i-flow" x="246" y="188" width="34" height="34"/>
    <use href="#i-gear" x="318" y="188" width="36" height="36"/>
  </g>
  <g stroke="#333" stroke-width="1.2"><line x1="105" y1="205" x2="140" y2="205"/><line x1="468" y1="205" x2="498" y2="205"/></g>
  <g class="lbl" fill="var(--ink)" font-size="9.5">
    <text x="300" y="143">Redaction</text>
    <text x="410" y="130">QA Check</text>
    <text x="80" y="236">E-discovery</text>
    <text x="190" y="236">Ingestion</text>
    <text x="262" y="236">Deduplication</text>
    <text x="336" y="236">Conversion</text>
    <text x="410" y="236">Redaction</text>
    <text x="527" y="236">Export</text>
  </g>
  <text class="foot" x="95" y="330">© 2023 TAVEXO. Public Security Policy | Privacy Policy</text>
</svg>
</section>

</body>
</html>
```